We are needed to get an artwork developed for a conference booth across 2 background panels. The design we’d like is of the tree from our existing Meadowlark Studio logo (included). Not wanting a black background.
In addition we’d like the title text
COMMUNITY RECOVERY
COMMUNITY RESILIENCE
A set of national principles
A community of practice
How can we shape the future together?

We are also wanting to have the following text in the roots of the tree.
- Understand the context
- Recognise complexity
- Use community-led approaches
- Coordinate all activities
- Communicate effectively
- Recognise and build capacity

Important – Artwork Requirements
Create 2 conference Digital Print Panels 985mmW x 2347mmH. The conference panels will be put together with a 5mm gap avoid small text in this area.
Print-ready artwork files are to be scaled at correct dimensions.
All artwork must be submitted no larger than 50% scale. Do not supply artwork files over 300MB for large images – Scaling to 50% @ 300 DPI is preferred.
No bleed required for panel prints.
All fonts must be outlined.
Overprint to be turned OFF.
Flatten all transparencies.
Supply as one single layer.
Embed all links.
PDF file submission
Please supply artwork to the exact specifications (dimension, text and images) and high resolution print-ready files.

```html
<!DOCTYPE html>
<html lang="en">
<head>
<meta charset="utf-8">
<title>Community Recovery, Community Resilience – Conference Panels</title>
<link rel="stylesheet" href="https://fonts.googleapis.com/css2?family=Exo+2:ital,wght@0,800;1,900&family=Raleway:wght@400;600&display=swap">
<style>
  :root {
    --page: #ffffff;
    --purple: #9b268a;
    --purple-deep: #7a246f;
    --sky: #2f97d4;
    --earth: #8f4440;
    --yellow: #fcd34a;
    --light-blue: #88c4ea;
    --green: #a8cf45;
    --blush: #f6dfe0;
    --white: #ffffff;
  }
  * { margin: 0; padding: 0; box-sizing: border-box; }
  html, body { width: 1079px; height: 1200px; overflow: hidden; background: var(--page); }
  .canvas { position: relative; width: 1079px; height: 1200px; }
  .panel { position: absolute; top: 63px; width: 451px; height: 1074px; overflow: hidden; }
  .panel--purple { left: 73px; --sky-tone: var(--purple); --ground-tone: var(--purple-deep); --title-second: var(--light-blue); }
  .panel--blue { left: 561px; --sky-tone: var(--sky); --ground-tone: var(--earth); --title-second: var(--white); }
  .panel__art { position: absolute; inset: 0; width: 451px; height: 1074px; }
  .sky { fill: var(--sky-tone); }
  .ground { fill: var(--ground-tone); }
  .swoosh { fill: none; stroke: var(--white); stroke-width: 3; stroke-linecap: round; }
  .line { position: absolute; left: 0; width: 100%; text-align: center; line-height: 1; white-space: nowrap; }
  .title { font-family: "Exo 2", sans-serif; font-weight: 800; font-size: 35px; letter-spacing: -1px; }
  .title--recovery { color: var(--yellow); }
  .title--resilience { color: var(--title-second); }
  .subtitle { font-family: "Raleway", sans-serif; font-weight: 600; font-size: 23.5px; color: var(--white); }
  .question { font-family: "Exo 2", sans-serif; font-weight: 900; font-style: italic; font-size: 22.5px; color: var(--yellow); }
  .principle { font-family: "Raleway", sans-serif; }
  .principle--small { font-weight: 600; font-size: 23px; }
  .principle--large { font-weight: 400; font-size: 32px; }
  .c-yellow { color: var(--yellow); }
  .c-blue { color: var(--light-blue); }
  .c-blush { color: var(--blush); }
  .c-green { color: var(--green); }
</style>
</head>
<body>
<main class="canvas">
  <section class="panel panel--purple">
    <svg class="panel__art" viewBox="0 0 451 1074">
      <defs>
        <radialGradient id="treeGlowA" cx="50%" cy="42%" r="50%">
          <stop offset="0" stop-color="#ffffff" stop-opacity="0.3"/>
          <stop offset="1" stop-color="#ffffff" stop-opacity="0"/>
        </radialGradient>
      </defs>
      <rect class="sky" width="451" height="1074"/>
      <path class="ground" d="M0 687 C90 694 170 664 246 664 C310 664 350 693 400 693 C425 693 440 691 451 689 L451 1074 L0 1074 Z"/>
      <path class="swoosh" d="M57 157 C92 144 140 138 183 147"/>
      <ellipse cx="227" cy="505" rx="160" ry="225" fill="url(#treeGlowA)" role="img" aria-label="White chalk-style line drawing of a leafy tree with roots spreading into the ground"/>
    </svg>
    <div class="line title title--recovery" style="top:54px">Community Recovery</div>
    <div class="line title title--resilience" style="top:96px">Community Resilience</div>
    <div class="line subtitle" style="top:173px">A set of national principles</div>
    <div class="line subtitle" style="top:199px">A community of practice</div>
    <div class="line question" style="top:231px">How can we shape the</div>
    <div class="line question" style="top:258px">future together?</div>
    <div class="line principle principle--small c-yellow" style="top:755px">Understand the context</div>
    <div class="line principle principle--large c-blue" style="top:791px">Recognise complexity</div>
    <div class="line principle principle--small c-blush" style="top:839px">Use community-led approaches</div>
    <div class="line principle principle--large c-green" style="top:875px">Coordinate all activities</div>
    <div class="line principle principle--small c-yellow" style="top:923px">Communicate effectively</div>
    <div class="line principle principle--large c-blue" style="top:962px">Recognise &amp; build capacity</div>
  </section>

  <section class="panel panel--blue">
    <svg class="panel__art" viewBox="0 0 451 1074">
      <defs>
        <radialGradient id="treeGlowB" cx="50%" cy="42%" r="50%">
          <stop offset="0" stop-color="#ffffff" stop-opacity="0.3"/>
          <stop offset="1" stop-color="#ffffff" stop-opacity="0"/>
        </radialGradient>
      </defs>
      <rect class="sky" width="451" height="1074"/>
      <path class="ground" d="M0 687 C90 694 170 664 246 664 C310 664 350 693 400 693 C425 693 440 691 451 689 L451 1074 L0 1074 Z"/>
      <path class="swoosh" d="M57 157 C92 144 140 138 183 147"/>
      <ellipse cx="227" cy="505" rx="160" ry="225" fill="url(#treeGlowB)" role="img" aria-label="White chalk-style line drawing of a leafy tree with roots spreading into the ground"/>
    </svg>
    <div class="line title title--recovery" style="top:54px">Community Recovery</div>
    <div class="line title title--resilience" style="top:96px">Community Resilience</div>
    <div class="line subtitle" style="top:173px">A set of national principles</div>
    <div class="line subtitle" style="top:199px">A community of practice</div>
    <div class="line question" style="top:231px">How can we shape the</div>
    <div class="line question" style="top:258px">future together?</div>
    <div class="line principle principle--small c-yellow" style="top:755px">Understand the context</div>
    <div class="line principle principle--large c-blue" style="top:791px">Recognise complexity</div>
    <div class="line principle principle--small c-blush" style="top:839px">Use community-led approaches</div>
    <div class="line principle principle--large c-green" style="top:875px">Coordinate all activities</div>
    <div class="line principle principle--small c-yellow" style="top:923px">Communicate effectively</div>
    <div class="line principle principle--large c-blue" style="top:962px">Recognise &amp; build capacity</div>
  </section>
</main>
</body>
</html>
```